Harborline Electrical Flyer

An eye catching flyer design which showcases the type of work we do in the electrical industry in Vancouver,BC. The final design should be simple and incorporate our logo. And present a high end company.

Electrical

```html
<!DOCTYPE html>
<html lang="en">
<head>
<meta charset="utf-8">
<title>Harborline Electrical Flyer</title>
<link href="https://fonts.googleapis.com/css2?family=Anton&family=Archivo+Black&family=Catamaran:wght@400;500;600;700&display=swap" rel="stylesheet">
<style>
:root{
  --yellow:#f4d60c;
  --gold:#d6b10e;
  --ink:#111111;
  --grey-dark:#3a3a3a;
  --steel-top:#9aa1a8;
  --steel-bottom:#5d646b;
  --white:#ffffff;
  --card-title:#f2d21a;
  --card-text:#e6e6e6;
  --hall-blue:#5f87b3;
  --hall-sky:#b9d3e6;
  --hall-glow:#f4f9fc;
}
*{margin:0;padding:0;box-sizing:border-box}
html,body{width:971px;height:1200px;overflow:hidden;background:var(--white)}
.flyer{position:relative;width:971px;height:1200px;background:var(--white);font-family:"Catamaran",sans-serif;color:var(--ink)}
.hero{position:absolute;left:0;top:505px;width:971px;height:400px;
  background:
    radial-gradient(ellipse 38% 22% at 50% 40%,rgba(255,255,255,.95),rgba(255,255,255,0) 100%),
    radial-gradient(ellipse 70% 55% at 50% 95%,rgba(255,255,255,1),rgba(255,255,255,0) 100%),
    linear-gradient(90deg,rgba(120,170,190,.35) 0%,rgba(255,255,255,0) 22%,rgba(255,255,255,0) 78%,rgba(120,170,190,.35) 100%),
    linear-gradient(180deg,var(--hall-blue) 0%,#8fb0cf 16%,var(--hall-sky) 36%,#dfeaf2 55%,var(--hall-glow) 75%,var(--white) 100%)}
.band{position:absolute;left:0;top:0}
.brand{position:absolute;left:86px;top:70px;display:flex;align-items:center;gap:14px}
.brand-dot{width:46px;height:46px;border-radius:50%;background:var(--yellow)}
.brand-name{font-weight:700;font-size:38px;line-height:1;color:#4a4a4a;letter-spacing:1px}
.contact-tab{position:absolute;left:598px;top:113px;width:282px;height:54px;background:var(--gold);border-radius:8px 8px 0 0;font-family:"Anton",sans-serif;font-size:38px;color:var(--white);text-align:center;line-height:54px;letter-spacing:1px}
.phone-box{position:absolute;left:577px;top:165px;width:328px;height:70px;background:linear-gradient(var(--steel-top),var(--steel-bottom));border-radius:0 0 12px 12px;border:2px solid #e8e8e8;font-family:"Anton",sans-serif;font-size:44px;color:var(--white);text-align:center;line-height:64px;letter-spacing:1px}
.services-title{position:absolute;left:53px;top:244px;font-family:"Anton",sans-serif;font-size:42px;color:var(--white);letter-spacing:2px;text-shadow:1px 2px 2px rgba(0,0,0,.35)}
.service-list{position:absolute;list-style:none;font-family:"Anton",sans-serif;font-size:27px;line-height:37px;letter-spacing:2px}
.service-list li{display:flex;align-items:center;gap:10px}
.service-list li::before{content:"";flex:none;width:22px;height:22px;border-radius:50%;background:radial-gradient(circle at 35% 35%,#ffffff,#b9b9b9);box-shadow:0 1px 2px rgba(0,0,0,.3)}
.col-a{left:50px;top:313px}
.col-b{left:271px;top:313px}
.intro{position:absolute;left:51px;top:484px;font-size:15.5px;font-weight:500;line-height:22px}
.divider{position:absolute;left:637px;top:262px;width:2px;height:225px;background:var(--gold)}
.tagline{position:absolute;left:660px;top:267px;font-family:"Anton",sans-serif;font-size:36px;line-height:45px;letter-spacing:2px}
.email{position:absolute;left:250px;top:785px;font-size:21px;font-weight:600;letter-spacing:.3px}
.website{position:absolute;left:250px;top:820px;font-family:"Archivo Black",sans-serif;font-size:36px;letter-spacing:.5px}
.about{position:absolute;left:51px;top:874px;width:112px;font-size:17.5px;font-weight:500;line-height:22.7px}
.card{position:absolute;top:880px;width:243px;height:282px;background:var(--grey-dark);box-shadow:0 3px 6px rgba(0,0,0,.35);text-align:center;padding:6px 6px 0}
.card-photo{height:145px;border:2px solid var(--yellow);border-radius:8px}
.card-title{margin-top:10px;font-size:18px;font-weight:600;line-height:20px;color:var(--card-title)}
.card-text{margin-top:5px;padding:0 12px;font-size:13px;line-height:16.5px;color:var(--card-text)}
.card-1{left:166px}.card-2{left:423px}.card-3{left:679px}
.card-1 .card-text{padding:0 14px}
.card-2 .card-text{padding:0 22px}
.card-3 .card-text{padding:0 4px;text-align:justify;text-align-last:center}
</style>
</head>
<body>
<div class="flyer">
  <div class="hero" role="img" aria-label="Photo of a bright, modern commercial hall with ceiling light slats, white pillars and a glossy reflective floor"></div>

  <svg class="band" width="971" height="545" viewBox="0 0 971 545">
    <path fill="#f4d60c" d="M0 180 H150 Q165 180 172 196 L178 210 Q184 222 200 222 H500 Q515 222 522 208 L528 196 Q535 180 555 180 H971 V538 H895 Q880 538 872 530 L865 523 Q858 516 845 516 H670 Q658 516 650 524 L642 532 Q636 538 620 538 H0 Z"/>
  </svg>

  <div class="brand">
    <span class="brand-dot"></span>
    <span class="brand-name">Harborline Electrical Inc</span>
  </div>

  <div class="contact-tab">CONTACT US</div>
  <div class="phone-box">604 555 0137</div>

  <h2 class="services-title">TYPES OF SERVICES</h2>
  <ul class="service-list col-a">
    <li>RESIDENTIAL</li><li>INDUSTRIAL</li><li>FIRE ALARM</li><li>SECURITY</li>
  </ul>
  <ul class="service-list col-b">
    <li>COMMERICAL</li><li>LIGHTING</li><li>LOW VOLTAGE WIRING</li><li>SOLAR PANEL</li>
  </ul>
  <p class="intro">Harborline Electrical offers a wide varierty of services, to meet your electrical needs.<br>Whether it may be residential, commercial or industrial.</p>

  <div class="divider"></div>
  <p class="tagline">RESIDENTIAL<br>COMMERCIAL<br>AND INDUSTRIAL<br>ELECTRICAL<br>SERVICES</p>

  <p class="email">info@HARBORLINEELECTRICAL.CA</p>
  <p class="website">wwwharborlineelectrical.ca</p>

  <p class="about">We are an<br>electrical<br>contractor<br>serving the<br>lower<br>mainland.<br>Providing<br>the best in<br>customer<br>service and<br>knowledge,<br>to our<br>clients.</p>

  <div class="card card-1">
    <div class="card-photo" role="img" aria-label="Photo of a warmly lit corridor with red and yellow light panels" style="background:linear-gradient(135deg,#c7721b,#e9b23a 45%,#9c2a1c)"></div>
    <h3 class="card-title">LIGHTING<br>EXPERTS</h3>
    <p class="card-text">We provide all your lighting needs to complete any project from small to large</p>
  </div>
  <div class="card card-2">
    <div class="card-photo" role="img" aria-label="Photo of an electrical panel with smart lighting controls" style="background:linear-gradient(90deg,#d9d2c4 0%,#d9d2c4 22%,#2a2a2e 22%,#2a2a2e 62%,#c9ccd0 62%)"></div>
    <h3 class="card-title">PANELIZED SMART<br>LIGHTING</h3>
    <p class="card-text">Smart lighting solutions give you endless options with your lights</p>
  </div>
  <div class="card card-3">
    <div class="card-photo" role="img" aria-label="Photo of an electrician in a plaid shirt holding a yellow hard hat and tool belt" style="background:linear-gradient(135deg,#b9b3ad,#8a6f5c 50%,#e0c21c)"></div>
    <h3 class="card-title">QUALITY ON TIME<br>CONSTRUCTION</h3>
    <p class="card-text">We efficiently manage construction and co odinate with schedules to always give our clients an effortless experience.</p>
  </div>
</div>
</body>
</html>
```